tidal box

TIDAL BOX mobile technology servicesPhone and tablet repairs, screens data recovery.

Industry/Entity Type

Data Recovery

Contact Information for Business Card

0491 573 086

Colors
33a6d7
f04a50
0a90cc
e34197

Requirements
Must have
• Liam hardy
Nice to have
• White background

```html
<!DOCTYPE html>
<html lang="en">
<head>
<meta charset="utf-8">
<title>Tidal Box – Business Card</title>
<link rel="stylesheet" href="https://fonts.googleapis.com/css2?family=Marcellus+SC&family=Questrial&display=swap">
<style>
  :root {
    --blue: #33a6d7;
    --blue-deep: #0a90cc;
    --red: #f04a50;
    --pink: #e34197;
    --ink: #2f3a3a;
    --paper: #ffffff;
    --edge: #eef0f2;
  }
  * { margin: 0; padding: 0; box-sizing: border-box; }
  html, body {
    width: 1200px;
    height: 742px;
    overflow: hidden;
    background: var(--edge);
  }
  .card {
    position: absolute;
    left: 12px;
    top: 12px;
    width: 1176px;
    height: 718px;
    background: var(--paper);
  }
  .phone-number {
    position: absolute;
    left: 66px;
    top: 70px;
    font-family: "Questrial", sans-serif;
    font-size: 50px;
    letter-spacing: 1px;
    color: var(--red);
  }
  .person {
    position: absolute;
    right: 90px;
    top: 20px;
    width: 320px;
    text-align: center;
    font-family: "Marcellus SC", serif;
  }
  .person-name {
    font-size: 92px;
    line-height: 1;
    color: var(--blue);
    letter-spacing: 2px;
  }
  .person-role {
    font-size: 46px;
    line-height: 1.15;
    color: var(--pink);
  }
  .device-artwork {
    position: absolute;
    left: 358px;
    top: 140px;
    width: 470px;
    height: 250px;
  }
  .brand-name {
    position: absolute;
    left: 0;
    top: 392px;
    width: 100%;
    text-align: center;
    font-family: "Questrial", sans-serif;
    font-size: 140px;
    line-height: 1;
    letter-spacing: 6px;
    color: var(--red);
  }
  .services {
    position: absolute;
    left: 0;
    top: 555px;
    width: 100%;
    text-align: center;
    font-family: "Marcellus SC", serif;
    color: var(--ink);
    font-size: 38px;
    line-height: 66px;
    letter-spacing: 1px;
  }
</style>
</head>
<body>
  <main class="card">
    <div class="phone-number">0491 573 086</div>

    <div class="person">
      <div class="person-name">Liam</div>
      <div class="person-role">Hardy</div>
    </div>

    <svg class="device-artwork" viewBox="0 0 470 250" role="img" aria-label="Illustration of a smartphone and a tablet with cracked screens">
      <defs>
        <linearGradient id="deviceTone" x1="0" y1="1" x2="1" y2="0">
          <stop offset="0" stop-color="#f04a50"/>
          <stop offset="1" stop-color="#33a6d7"/>
        </linearGradient>
      </defs>
      <rect x="0" y="0" width="470" height="250" rx="18" fill="url(#deviceTone)" opacity="0.55"/>
    </svg>

    <div class="brand-name">TIDAL BOX</div>

    <div class="services">
      <p>Mobile technology services</p>
      <p>Phone &amp; tablet repairs, data recovery.</p>
    </div>
  </main>
</body>
</html>
```